Business Card Design: recruitment/consultancy for business Marlowin730go

We need a business card design for a new company based in Adelaide Australia called Marlowin730go. Our Business aims to support people over 50 who may be looking for a career change, have been made redundant or generally looking for employment. We will also be working with businesses to provide them with recruiting solutions, job design, recruitment strategies and customised training. we will also be working with volunteering opportunities for those over 50.
We would like to see the E in marlowin730go strong and dominant. The final design should reflect change for the better, better opportunities, today is the day, make way for the new, all aimed at the 50 plus age group.
Colours we are thinking off include green (money, growth) black and white.... we like the idea of black and white photography with a one dominant colour...think of a of a black and white photo of a woman with dominant red lips...that sort of look

Industry/Entity Type

Business

Contact Information for Business Card

Dale, Wendy & Gwen
phone: 0498613205
Marlowin730go@quillmarsh.net
Facebook/Marlowin730go
www.marlowin730go.net.au

```html
<!DOCTYPE html>
<html lang="en">
<head>
<meta charset="utf-8">
<title>Marlowin730go business card</title>
<link rel="stylesheet" href="https://fonts.googleapis.com/css2?family=PT+Serif:wght@400;700&family=Arimo:wght@400&display=swap">
<style>
  :root {
    --backdrop: #e9e7e3;
    --card: #ffffff;
    --card-shade: #f1f1f1;
    --green: #5cbb3c;
    --charcoal: #3b3b3d;
    --band: #231b1c;
    --ink: #1d1d1d;
    --text-grey: #5a5a5a;
    --photo-dark: #8d8d8d;
    --photo-light: #e4e4e4;
  }
  * { margin: 0; padding: 0; box-sizing: border-box; }
  html, body { width: 1200px; height: 858px; overflow: hidden; }
  body { background: var(--backdrop); position: relative; font-family: "Arimo", Arial, sans-serif; }

  .card {
    position: absolute;
    width: 560px; height: 342px;
    background: linear-gradient(135deg, var(--card) 55%, var(--card-shade));
    box-shadow: 0 10px 28px rgba(0,0,0,.22);
    overflow: hidden;
  }
  .card--front { left: 60px; top: 70px; }
  .card--back { left: 580px; top: 446px; }

  /* front */
  .edge-strip { position: absolute; left: 0; top: 0; width: 14px; height: 100%; }
  .edge-strip__green { height: 62%; background: var(--green); }
  .edge-strip__dark { height: 38%; background: var(--charcoal); }

  .portrait {
    position: absolute; right: 0; top: 0; width: 300px; height: 230px;
    background: linear-gradient(200deg, var(--photo-dark) 0%, #b5b5b5 40%, var(--photo-light) 75%, rgba(255,255,255,0) 100%);
  }

  .brand {
    position: absolute; left: 40px; top: 52px;
    font-family: "PT Serif", Georgia, serif; font-weight: 700;
    font-size: 40px; letter-spacing: -0.5px; color: var(--ink);
  }

  .details { position: absolute; left: 42px; top: 168px; color: var(--text-grey); }
  .details__names { font-size: 19px; margin-bottom: 14px; letter-spacing: .2px; }
  .details__list { list-style: none; }
  .details__item { display: flex; align-items: center; gap: 10px; font-size: 15px; line-height: 24px; }
  .details__icon { width: 12px; height: 12px; flex: none; }

  /* back */
  .back-band {
    position: absolute; left: 0; top: 112px; width: 100%; height: 92px;
    background: var(--band);
    display: flex; align-items: center; padding-left: 150px;
  }
  .back-band__name {
    font-family: "PT Serif", Georgia, serif; font-weight: 400;
    font-size: 34px; color: #ffffff; letter-spacing: .5px;
  }
</style>
</head>
<body>

<section class="card card--front">
  <div class="edge-strip">
    <div class="edge-strip__green"></div>
    <div class="edge-strip__dark"></div>
  </div>
  <div class="portrait" role="img" aria-label="Black and white portrait photograph of a woman with red lips"></div>

  <div class="brand">Marlowin730go</div>

  <div class="details">
    <p class="details__names">Dale, Wendy &amp; Gwen</p>
    <ul class="details__list">
      <li class="details__item">
        <svg class="details__icon" viewBox="0 0 12 12"><path d="M1 3c0-1 1-2 2-2h6c1 0 2 1 2 2v1H8V3H4v1H1z M2 5h8l1 6H1z" fill="#666"/></svg>
        0498613205
      </li>
      <li class="details__item">
        <svg class="details__icon" viewBox="0 0 12 12"><rect x="0.5" y="2" width="11" height="8" fill="#666"/><path d="M0.5 2l5.5 4.5L11.5 2" stroke="#fff" stroke-width="1" fill="none"/></svg>
        Marlowin730go@quillmarsh.net
      </li>
      <li class="details__item">
        <svg class="details__icon" viewBox="0 0 12 12"><rect x="1" y="1" width="10" height="10" rx="1.5" fill="#666"/></svg>
        Marlowin730go
      </li>
      <li class="details__item">
        <svg class="details__icon" viewBox="0 0 12 12"><circle cx="6" cy="6" r="5.2" fill="none" stroke="#666" stroke-width="1.2"/><ellipse cx="6" cy="6" rx="2.2" ry="5.2" fill="none" stroke="#666" stroke-width="1"/><path d="M1 6h10" stroke="#666" stroke-width="1"/></svg>
        www.marlowin730go.net.au
      </li>
    </ul>
  </div>
</section>

<section class="card card--back">
  <div class="back-band">
    <span class="back-band__name">Marlowin730go</span>
  </div>
</section>

</body>
</html>
```